A4 double sided brochure for progressive, young lawyers

Hi designers, we would like a double sided A4 flyer advertising:

Designers, Side 1 flyer contents:

Main heading #1 on side 1: Wills

A comprehensive, legal Will gives you peace of mind.

It ensures that your wealth is distributed according to your wishes.

As your life changes, so should your Will. It should reflect evolving circumstances, such as:
- separation or divorce
- assets disposed of or acquired
- the birth or death of beneficiaries
- minor beneficiaries coming of age
- the death or incapacity of an executor

Our lawyers will listen to your wishes and provide tailored advice to suit your needs.

Main heading #2 on side 1 : Testamentary Discretionary Trusts

Did you know that your beneficiaries may have to pay tax on property you leave them in your Will? You can better protect them and minimise potential tax by income streaming with testamentary discretionary trusts.

(Note to Designers: I have attached a word document containing information that I would like to appear under this sentence which includes a few paragraphs and a data table. Please include all information from the word document here in a similar kind or format.)

(Our Call to Action): K.T. Marlow Lawyers has a team of experienced lawyers who can advise you on drafting an effective Will.

Call or email one of our friendly Principals, Rohan Marlow or Priya Marlow for a quick, no-obligation quote.

Designers, side 2 flyer content is as follows:

Main heading side 2: Planning Ahead

Estate Planning is not just about having a Will.

It involves your personal, family and business matters, both now and after you pass away.

While it may be as simple as having a Will, it most cases it also involves having Powers of Attorney, Enduring Guardianships and Advance Health Care planning.

Estate planning is about planning ahead for your current lifestyle needs, you retirement plans, your business arrangements, your tax and superannuation position, future events (like divorce, ill-health and family disputes) and ultimately, ensuring your assets go exactly where you want them to.

Simply put, it gives you peace of mind.

Heading #2 on side 2: What else should I consider now?

[Designers, I am happy for you to put the below 3 points into a picture diagram or some kind of list format - whatever looks less boring!

1. A Power of Attorney - This enables you to appoint a trusted person to act on your behalf if you are unable to, or simply don’t wish to, make decisions about your financial and legal affairs.

[DESIGNERS - please highlight, enlarge or emphasize the words 'power of attorney']

2. A Power of Enduring Guardianship - This enables you to appoint a trusted person to act on your behalf if you are unable (through mental incapacity) to make decisions about your health and welfare issues.

[DESIGNERS - please somehow highlight the words 'power of enduring guardianship']

3. An Advance Health Care Plan - This directs your doctors, medical staff and family how you wish to be treated. Remember, you have the right to accept or refuse medical treatment.

[DESIGNERS - please highlight the words 'Advance Health Care Plan']

(Our Call to Action):

K.T. Marlow Lawyers has a team of experienced lawyers who can advise you on preparing a Will, Powers of Attorney and Powers of Enduring Guardianship, estate planning and administration of a deceased estate.

Industry/Entity Type

Legal

Font styles to use
Sans Serif

Requirements
Must have
• Colours should match our logo. See our website www.ktmarlow.com.au also for colours. Please not too much red blocks areas though.
• Our firm name is: K.T. Marlow Lawyers
• Note to designers - Both sides should have contact details of our 2 offices and other contact information including:
• For more information contact our Principals:
• Rohan Marlow or Priya Marlow
• Office locations:
• ASHWOOD PARK:
• Shop 5, 14-32 Dunmore Crescent,
• Ashwood Park NSW 2219
• Phone: (02) 9384 2175
• LINDEN VALE:
• 7 Kestrel Lane,
• Linden Vale NSW
• Phone: (02) 9673 4809
• Email: admin@ktmarlow.com.au
• Web: www.ktmarlow.come.au
• Connect with us on Facebook:
• www.facebook.com/ktmarlowlawyers
• Must have 2 pages (back and front of flyer). See project description for details.
• I would like all information contained in the project description and all information contained in my word doc attached to be included in the brochure. Please do not edit the words or the structure of the information.
• The data table (in the word doc attached) must be replicated exactly as it appears including the fine print.
Should not have
• Too many block red areas or too much red.
• I want it to be eye catching but not too bright to read.

```html
<!DOCTYPE html>
<html lang="en">
<head>
<meta charset="utf-8">
<title>K.T. Marlow Lawyers – Wills &amp; Planning Ahead Flyer</title>
<link href="https://fonts.googleapis.com/css2?family=Oswald:wght@500;700&family=Roboto+Condensed:wght@300;400;700&display=swap" rel="stylesheet">
<style>
:root{
  --red:#a8232b;
  --yellow:#f7dc1d;
  --ink:#222;
  --grey-arrow:#c9c9c9;
  --backdrop:#3c3c3c;
  --white:#fff;
}
*{margin:0;padding:0;box-sizing:border-box}
html,body{width:1200px;height:1200px;overflow:hidden}
body{background:var(--backdrop);font-family:"Roboto Condensed",Arial,sans-serif;color:var(--ink);position:relative}
.page{position:absolute;background:var(--white);width:510px;height:722px;overflow:hidden}
.page--front{left:66px;top:60px}
.page--back{left:634px;top:357px}
.abs{position:absolute}

.brand{left:28px;top:30px;color:var(--red);font-weight:400;font-size:22px;letter-spacing:.5px;white-space:nowrap}
.hero-visual{left:232px;top:8px;width:278px;height:140px;background:linear-gradient(200deg,#f4efe9 0%,#b98a5a 45%,#5a3019 80%,#f3f0ec 100%);border-radius:4px}
.title{font-family:"Oswald",Impact,sans-serif;font-weight:700;color:var(--red);line-height:1}
.title--wills{left:24px;top:102px;font-size:50px}
.lede{left:24px;font-weight:300;font-size:19px;line-height:1.1;color:var(--ink)}

.changes{left:0;top:231px;width:254px;height:217px;background:var(--red);padding:5px 4px 0 24px}
.changes__lead,.changes__close{color:var(--yellow);font-weight:700;font-size:12.6px;line-height:18px}
.changes__list{list-style:none;margin:3px 0 2px}
.changes__list li{color:var(--white);font-size:11.5px;line-height:23.4px;position:relative;padding-left:16px}
.changes__list li::before{content:"";position:absolute;left:0;top:9px;width:6px;height:6px;border-radius:50%;background:var(--white)}
.changes__close{font-size:12.8px;line-height:17px}

.title--trusts{left:272px;top:256px;font-size:34px;line-height:36px}
.trusts-intro{left:272px;top:368px;width:218px;font-size:9.2px;line-height:12.4px;text-align:justify}

.section-head{color:var(--red);font-weight:700;font-size:12px}
.streaming-head{left:0;width:100%;top:456px;text-align:center}
.streaming-body{left:24px;top:472px;width:462px;font-size:6.9px;line-height:10px}
.example-head{left:24px;top:515px}
.rates-head{left:320px;top:515px}

.arrow{left:22px;top:532px;width:286px;height:76px}
.example-table{left:28px;top:538px;width:228px;border-collapse:collapse;font-size:7.2px;line-height:9.2px;text-align:center}
.example-table td{border:1px solid #888;padding:2px;vertical-align:top}
.tax-saved{left:112px;top:612px;color:var(--red);font-weight:700;font-size:11px}

.rates{left:321px;top:532px;width:166px;border-collapse:collapse;font-size:7.3px;text-align:center}
.rates th,.rates td{border:1px solid #555;height:12px;padding:0 2px}
.rates th{font-weight:700;font-size:7px;height:18px;line-height:7px}
.rates td.hl{background:var(--red);color:var(--white)}

.disclaimer{left:0;width:100%;top:635px;text-align:center;font-size:6.3px;line-height:8px}

.footer{left:0;bottom:0;width:100%;height:70px;background:var(--red);color:var(--white);display:flex;align-items:center;justify-content:center;padding:0 8px;font-size:8px;line-height:10.6px;text-align:center}
.footer__col{padding:0 10px;border-right:1px solid rgba(255,255,255,.8)}
.footer__col:last-child{border-right:0}
.footer strong{font-weight:700}
.footer__contact{width:112px}
.footer__contact .names{font-size:8.6px;line-height:12.6px}

.title--plan{left:23px;top:20px;font-size:48px}
.back-body{left:23px;width:465px;font-size:8.6px;line-height:12.4px;text-align:justify}
.simply{left:23px;top:250px;font-weight:700;font-size:19px}
.title--else{left:24px;top:272px;font-size:35px;line-height:34px}
.consider{left:0;top:341px;width:100%;height:212px;background:linear-gradient(90deg,#c8bcae 0%,#8c6f52 18%,#d9d4ce 36%,#eeecea 55%,#f7f6f5 100%)}
.options{left:205px;top:344px;width:280px}
.option__name{font-weight:700;font-size:12.6px;margin-bottom:6px}
.option__text{font-size:9.3px;line-height:12.4px;margin-bottom:8px}
.cta{left:24px;top:562px;width:465px;font-weight:300;font-size:12.2px;line-height:15.6px}
.cta-call{left:0;width:100%;top:618px;text-align:center;color:var(--red);font-weight:700;font-size:12.6px;line-height:16px}
</style>
</head>
<body>

<section class="page page--front" aria-label="Flyer side one: Wills">
  <div class="abs brand">K.T. Marlow Lawyers</div>
  <div class="abs hero-visual" role="img" aria-label="Wooden judge's gavel resting on its sound block"></div>

  <h1 class="abs title title--wills">Wills</h1>
  <p class="abs lede" style="top:156px">A comprehensive, legal Will gives you peace of mind.</p>
  <p class="abs lede" style="top:182px">It ensures that your wealth is distributed<br>according to your wishes.</p>

  <div class="abs changes">
    <p class="changes__lead">As your life changes, so should your Will.<br>It should reflect evolving circumstances,<br>such as</p>
    <ul class="changes__list">
      <li>Separation or divorce</li>
      <li>Assets disposed of or acquired</li>
      <li>The birth or death of beneficiaries</li>
      <li>Minor beneficiaries coming of age</li>
      <li>The death or incapacity of an executor</li>
    </ul>
    <p class="changes__close">Our lawyers will listen to your wishes and provide tailored advice to suit your needs.</p>
  </div>

  <h2 class="abs title title--trusts">TESTAMENTARY<br>DISCRETIONARY<br>TRUSTS</h2>
  <p class="abs trusts-intro">Did you know that your beneficiaries may have to pay tax on property you leave them in your Will? You can better protect them and minimise potential tax by income streaming with testamentary discretionary trusts.</p>

  <h3 class="abs section-head streaming-head">Income streaming with testamentary discretionary trusts</h3>
  <p class="abs streaming-body">When a beneficiary in your Will earns income from a gift-eg. rent on an investment property, or capital gains when they sell it - that income will be taxable. While they have children under 18 years old, that income can be ‘streamed’ to the kids to take advantage of their preferential tax rates. This requires a special structure called a ‘testamentary discretionary trust’ that can only be created under a Will.</p>

  <h3 class="abs section-head example-head">Mary earns $180K salary and has 4 kids under 18 years old</h3>
  <h3 class="abs section-head rates-head">Income tax rates for resident minors</h3>

  <svg class="abs arrow" viewBox="0 0 286 76" aria-hidden="true"><polygon points="0,4 250,4 250,0 286,38 250,76 250,72 0,72" fill="var(--grey-arrow)"/></svg>
  <table class="abs example-table">
    <tr>
      <td>Jane leaves an investment property worth $1M to her daughter Mary</td>
      <td>Five years later, Mary sells the property for $1.3M, making a $300K capital gain</td>
      <td style="width:96px">Using a ‘simple’ Will :<br>Tax = 47% x $300K = $141K<br>Using a Testamentary Trust :<br>($75K streamed to each child)<br>Tax =$15,922 x 4 = $63,688</td>
    </tr>
  </table>
  <p class="abs tax-saved">TAX SAVED: $77,312</p>

  <table class="abs rates">
    <tr><th>Distribution ($)</th><th>Family Trust</th><th>Testamentary<br>Trust</th></tr>
    <tr><td>0 – 416</td><td></td><td></td></tr>
    <tr><td>417 – 1,307</td><td>66%*</td><td></td></tr>
    <tr><td>1,308 – 18,200</td><td>47%*</td><td></td></tr>
    <tr><td>1,308 – 18,200</td><td>47%*</td><td class="hl">19%</td></tr>
    <tr><td>37,001 – 80,000</td><td>47%*</td><td class="hl">32.5%</td></tr>
    <tr><td>80,001 – 180,000</td><td>47%*</td><td class="hl">37%</td></tr>
  </table>

  <p class="abs disclaimer">This document contains only a summary of a discrete part of law and is correct at the date of publication. It is<br>not legal advice. You should always seek legal advice about your individual situation.</p>

  <footer class="abs footer">
    <div class="footer__col footer__contact"><strong>For more information<br>contact our Principals</strong><div class="names"><strong>Rohan Marlow<br>Priya Marlow</strong></div></div>
    <div class="footer__col"><strong>ASHWOOD PARK</strong><br>Shop 5, 14-32 Dunmore Crescent,<br>Ashwood Park NSW 2219<br><strong>(02) 9384 2175</strong></div>
    <div class="footer__col"><strong>LINDEN VALE</strong><br>7 Kestrel Lane,<br>Linden Vale NSW<br><strong>(02) 9673 4809</strong></div>
    <div class="footer__col">admin@ktmarlow.com.au<br>www.ktmarlow.come.au<br>www.facebook.com/ktmarlowlawyers</div>
  </footer>
</section>

<section class="page page--back" aria-label="Flyer side two: Planning Ahead">
  <h1 class="abs title title--plan">Planning Ahead</h1>
  <p class="abs lede" style="left:23px;top:76px">Estate Planning is not just about having a Will.</p>
  <p class="abs lede" style="left:23px;top:104px">It involves your personal, family and business matters,<br>both now and after you pass away.</p>
  <p class="abs back-body" style="top:161px">While it may be as simple as having a Will, it most cases it also involves having Powers of Attorney, Enduring Guardianships and Advance Health Care planning.</p>
  <p class="abs back-body" style="top:197px">Estate planning is about planning ahead for your current lifestyle needs, you retirement plans, your business arrangements, your tax and superannuation position, future events (like divorce, ill-health and family disputes) and ultimately, ensuring your assets go exactly where you want them to.</p>
  <p class="abs simply">Simply put, it gives you peace of mind</p>
  <h2 class="abs title title--else">WHAT ELSE<br>SHOULD I CONSIDER NOW?</h2>

  <div class="abs consider" role="img" aria-label="Bronze Lady Justice statue holding scales, beside a softly blurred office desk"></div>
  <div class="abs options">
    <h3 class="option__name">A Power of Attorney</h3>
    <p class="option__text">&nbsp;This enables you to appoint a trusted person to act on your behalf if you are unable to, or simply don’t wish to, make decisions about your financial and legal affairs.</p>
    <h3 class="option__name">A Power of Enduring Guardianship</h3>
    <p class="option__text">This enables you to appoint a trusted person to act on your behalf if you are unable (through mental incapacity) to make decisions about your health and welfare issues.</p>
    <h3 class="option__name">An Advance Health Care Plan</h3>
    <p class="option__text">This directs your doctors, medical staff and family how you wish to be treated. Remember, you have the right to accept or<br>refuse medical treatment.</p>
  </div>

  <p class="abs cta">K.T. Marlow Lawyers has a team of experienced lawyers who can advise you on preparing a Will, Powers of Attorney and Powers of Enduring Guardianship, estate planning and administration of a deceased estate.</p>
  <p class="abs cta-call">Call or email one of our friendly Principals,<br>Rohan Marlow or Priya Marlow for a quick, no-obligation quote.</p>

  <footer class="abs footer">
    <div class="footer__col footer__contact"><strong>For more information<br>contact our Principals</strong><div class="names"><strong>Rohan Marlow<br>Priya Marlow</strong></div></div>
    <div class="footer__col"><strong>ASHWOOD PARK</strong><br>Shop 5, 14-32 Dunmore Crescent,<br>Ashwood Park NSW 2219<br><strong>(02) 9384 2175</strong></div>
    <div class="footer__col"><strong>LINDEN VALE</strong><br>7 Kestrel Lane,<br>Linden Vale NSW<br><strong>(02) 9673 4809</strong></div>
    <div class="footer__col">admin@ktmarlow.com.au<br>www.ktmarlow.come.au<br>www.facebook.com/ktmarlowlawyers</div>
  </footer>
</section>

</body>
</html>
```